Website design project for ICT Business - Harbor Link Ko

We need website built for our new startup. The company name is Harbor Link KO. Harbor Link is an Information Communication Technology business that aims to help small to medium businesses unlock the power and benefits of the cloud. We are a sales and support business that consults with our clients to assist them in migrating to the cloud safely and without business interruption.

Coding

Coded - Design and coding required

Number of Pages Required

4 page

```html
<!DOCTYPE html>
<html lang="en">
<head>
<meta charset="utf-8">
<title>Harbor Link — ICT Based Business</title>
<link href="https://fonts.googleapis.com/css2?family=Figtree:wght@300;400;600;700&family=Lato:ital,wght@0,400;0,700;1,400&display=swap" rel="stylesheet">
<style>
:root{
  --navy:#0a5796;
  --navy-dark:#074d86;
  --sky:#00aeef;
  --ink:#333;
  --muted:#5a5a5a;
  --band:#f3f3f3;
  --line:#d4d4d4;
  --white:#fff;
}
*{box-sizing:border-box;margin:0;padding:0}
html,body{width:1200px;height:2542px;overflow:hidden;background:var(--white)}
body{position:relative;font-family:"Lato",Arial,sans-serif;color:var(--ink)}
.abs{position:absolute}
.heading{font-family:"Figtree",Arial,sans-serif;font-weight:400}
.btn{position:absolute;background:var(--navy);color:var(--white);font:700 15px "Lato",sans-serif;display:flex;align-items:center;justify-content:center;text-transform:uppercase}

/* header */
.topline{top:0;left:0;width:1200px;height:4px;background:var(--navy)}
.brand{left:76px;top:62px;font:700 40px "Figtree",sans-serif;color:var(--navy);letter-spacing:-0.5px}
.callus{left:830px;top:17px;display:flex;align-items:center;gap:14px;font-size:17px;color:var(--ink)}
.callus b{font-weight:400;color:var(--sky);font-size:22px}
.callus .ring{width:42px;height:42px;border:2px solid var(--navy);border-radius:50%;display:flex;align-items:center;justify-content:center}
.nav{top:63px;left:556px;display:flex;align-items:center;font-size:17px;color:var(--sky)}
.nav a{color:var(--sky);text-decoration:none;height:40px;display:flex;align-items:center;justify-content:center}
.nav .home{width:80px;border:2px solid var(--sky)}
.nav .login{background:var(--sky);color:var(--white);width:80px;font-weight:700}

/* hero */
.hero{top:125px;left:0;width:1200px;height:553px;background:linear-gradient(180deg,#9ec6e6 0%,#cfe3f2 38%,#b8c9d6 62%,#6d879b 100%)}
.hero-shadow{top:676px;left:0;width:1200px;height:20px;background:radial-gradient(ellipse at top,rgba(0,0,0,.18),transparent 70%)}
.hero .arrow{position:absolute;top:258px;color:var(--navy)}
.hero-copy{left:571px;top:250px;color:var(--navy)}
.hero-copy .pre{font:400 28px "Lato",sans-serif}
.hero-copy h1{font:700 64px "Lato",sans-serif;letter-spacing:-1px;line-height:1.05;margin-top:2px}
.hero-copy p{font-size:21px;line-height:31px;color:#4a4a4a;width:520px;margin-top:16px}
.hero-copy p b{color:#3d3d3d}

/* welcome */
.section-title{width:1200px;left:0;text-align:center;font-size:40px;color:var(--navy)}
.section-title span{color:var(--sky)}
.welcome-text{left:80px;top:783px;width:535px;font-size:15.5px;line-height:23px;color:#444}
.welcome-text p{margin-bottom:23px}
.welcome-media{left:685px;top:792px;width:437px;height:259px;background:linear-gradient(135deg,#6f97c7,#c5d9ee 45%,#8aa9d6 70%,#cdb7e6)}
.play{position:absolute;left:190px;top:101px;width:56px;height:56px;border-radius:50%;background:rgba(80,80,80,.7);display:flex;align-items:center;justify-content:center}

/* services */
.services{top:1105px;left:0;width:1200px;height:488px;background:var(--band)}
.service{position:absolute;top:1229px;width:250px;text-align:center}
.service .disc{width:125px;height:125px;border-radius:50%;margin:0 auto;display:flex;align-items:center;justify-content:center}
.service h3{font:400 23px "Figtree",sans-serif;color:#222;margin-top:28px;text-transform:uppercase}
.service p{font-size:15.5px;line-height:23px;color:var(--muted);margin:10px auto 0;width:236px}
.service .btn{position:relative;width:125px;height:51px;margin:18px auto 0}

/* news & quote */
.block-title{font-size:36px;color:var(--sky)}
.block-title span{color:var(--navy)}
.news-item{position:absolute;left:78px;width:480px;height:102px}
.news-item .thumb{position:absolute;left:0;top:0;width:102px;height:102px;border:1px solid var(--line);padding:4px}
.news-item .thumb div{width:100%;height:100%;background:linear-gradient(160deg,#c9d8e4,#7f98aa 55%,#dfe6eb)}
.news-item h4{position:absolute;left:120px;top:2px;font:400 19px "Lato",sans-serif;color:#222}
.news-item p{position:absolute;left:120px;top:32px;font-size:14.5px;line-height:23px;color:var(--muted);width:360px}
.news-item a{position:absolute;left:120px;top:82px;font-size:14.5px;color:var(--navy);text-decoration:none;text-transform:uppercase}
.field{position:absolute;border:1px solid var(--line);border-radius:3px;background:var(--white);font-size:14px;color:#666;padding:10px 12px}

/* testimonial */
.testimonial{top:1932px;left:0;width:1200px;height:266px;background:var(--sky)}
.avatar{position:absolute;left:195px;top:98px;width:115px;height:115px;border-radius:50%;border:4px solid var(--white);background:linear-gradient(160deg,#d9d3cf,#a39b96)}
.quote-mark{position:absolute;font:700 120px Georgia,serif;color:rgba(255,255,255,.45);line-height:1}
.quote-text{position:absolute;left:334px;top:100px;width:720px;font:italic 16px/25px "Lato",sans-serif;color:var(--white)}
.quote-name{position:absolute;left:334px;top:183px;font:400 21px "Figtree",sans-serif;color:var(--white)}
.quote-name small{font:700 14px "Lato",sans-serif}

/* footer */
.foot-title{font:400 20px "Figtree",sans-serif;color:var(--navy);display:flex;align-items:center;gap:14px}
.foot-title i{display:block;width:44px;height:1px;background:var(--sky)}
.quick-links{left:80px;top:2281px;width:112px;list-style:none;font-size:14px;color:var(--muted)}
.quick-links li{height:31px;line-height:31px;border-bottom:1px solid #e6e6e6}
.quick-links li.active{color:var(--sky)}
.contact-row{position:absolute;left:344px;display:flex;gap:14px;font-size:14.5px;line-height:22px;color:var(--muted)}
.map{left:607px;top:2239px;width:208px;height:207px;background:linear-gradient(150deg,#e4e7d8,#c9d8b9 50%,#e9e7dc);border:1px solid var(--line)}
.foot-brand{left:897px;top:2318px;width:200px;text-align:center;font:700 32px "Figtree",sans-serif;color:var(--navy)}
.social{left:937px;top:2388px;display:flex;gap:6px}
.social span{width:34px;height:34px;border-radius:50%;border:2px solid var(--navy)}
.social span:first-child{background:var(--navy)}
.copyright{top:2478px;left:0;width:1200px;height:64px;background:var(--navy-dark);color:var(--white);font-size:14px;display:flex;align-items:center;justify-content:center}
.copyright span{color:var(--sky);margin:0 4px}
</style>
</head>
<body>

<header>
  <div class="abs topline"></div>
  <div class="abs brand">Harbor Link</div>
  <div class="abs callus">
    <span class="ring"><svg width="18" height="18" viewBox="0 0 24 24"><path d="M6.6 10.8a15.1 15.1 0 0 0 6.6 6.6l2.2-2.2c.3-.3.7-.4 1-.2 1.1.4 2.3.6 3.6.6.6 0 1 .4 1 1V20c0 .6-.4 1-1 1A17 17 0 0 1 3 4c0-.6.4-1 1-1h3.5c.6 0 1 .4 1 1 0 1.3.2 2.5.6 3.6.1.3 0 .7-.2 1z" fill="none" stroke="#0a5796" stroke-width="1.6"/></svg></span>
    Call Us Now : <b>555-0142-770</b>
  </div>
  <nav class="abs nav">
    <a class="home">Home</a>
    <a style="width:100px">About</a>
    <a style="width:102px">Service</a>
    <a style="width:82px">News</a>
    <a style="width:110px">Contact</a>
    <a class="login">LOGIN</a>
  </nav>
</header>

<section class="abs hero" role="img" aria-label="City skyline with high-rise towers along a river under a bright cloudy sky">
  <svg class="arrow" style="left:32px" width="14" height="30" viewBox="0 0 14 30"><path d="M12 2 2 15l10 13" fill="none" stroke="#0a5796" stroke-width="2"/></svg>
  <svg class="arrow" style="left:1155px" width="14" height="30" viewBox="0 0 14 30"><path d="M2 2l10 13L2 28" fill="none" stroke="#0a5796" stroke-width="2"/></svg>
</section>
<div class="abs hero-shadow"></div>
<div class="abs hero-copy">
  <div class="pre">WE ARE AN</div>
  <h1>ICT Based Business</h1>
  <p><b>Cloud and Proud –</b> Ask us why more and more small businesses are moving their IT systems and software to the cloud</p>
</div>
<div class="btn" style="left:570px;top:470px;width:164px;height:51px;font-size:16px">Join us now</div>

<h2 class="abs section-title heading" style="top:712px">Welcome to <span>Harbor</span> Link</h2>
<div class="abs welcome-text">
  <p><b>Put down that pen and paper and get ready to embrace everything digital!</b></p>
  <p>IT is changing. FAST! Here at Harbor Link we want to help you not only survive in this environment but thrive. Stand out from your competitors with how you leverage software and applications to deliver an amazing experience to your customers.</p>
  <p>'Cash is King' - We assist businesses to hang on to their hard-earned capital in favour of a license based 'per user' monthly fee.</p>
</div>
<div class="btn" style="left:76px;top:1000px;width:146px;height:51px">Read more</div>
<div class="abs welcome-media" role="img" aria-label="Video still of a hand touching a network of connected clouds">
  <span class="play"><svg width="20" height="22" viewBox="0 0 20 22"><path d="M3 2l15 9-15 9z" fill="#fff"/></svg></span>
</div>

<section class="abs services"></section>
<h2 class="abs section-title heading" style="top:1152px"><span>Harbor</span> Link Services</h2>

<div class="service" style="left:83px">
  <div class="disc" style="background:var(--navy)"><svg width="70" height="50" viewBox="0 0 70 50"><path d="M18 40h-2a12 12 0 0 1 0-24 16 16 0 0 1 31-4 12 12 0 0 1 9 23 10 10 0 0 1-4 5H44" fill="none" stroke="#fff" stroke-width="2.4"/><path d="M31 46V24m-8 8 8-8 8 8" fill="none" stroke="#fff" stroke-width="2.4"/></svg></div>
  <h3>Cloud Services</h3>
  <p>Suite 360 – Northwind's leading cloud product. Get the benefit of a suite of cloud services...</p>
  <div class="btn">Read more</div>
</div>
<div class="service" style="left:345px">
  <div class="disc" style="background:var(--sky)"><svg width="64" height="58" viewBox="0 0 64 58"><path d="M6 54h8V38H6zm13 0h8V30h-8zm13 0h8V22h-8zm13 0h8V14h-8z" fill="#fff"/><path d="M4 32 50 6" stroke="#fff" stroke-width="3"/><path d="M42 3l14 0-5 12z" fill="#fff"/></svg></div>
  <h3>Digital Marketing</h3>
  <p>Logo and graphic design – Got an idea for a business, let us design the perfect logo, business...</p>
  <div class="btn">Read more</div>
</div>
<div class="service" style="left:605px">
  <div class="disc" style="background:var(--navy)"><svg width="76" height="50" viewBox="0 0 76 50"><g fill="#fff"><circle cx="38" cy="14" r="8"/><path d="M24 40c0-10 6-15 14-15s14 5 14 15z"/><circle cx="16" cy="22" r="6"/><path d="M4 46c0-8 5-12 12-12s12 4 12 12z"/><circle cx="60" cy="22" r="6"/><path d="M48 46c0-8 5-12 12-12s12 4 12 12z"/></g></svg></div>
  <h3>IT Support</h3>
  <p>Managed services – Get the benefits of in-house IT for a fraction of the cost...</p>
  <div class="btn">Read more</div>
</div>
<div class="service" style="left:867px">
  <div class="disc" style="background:var(--sky)"><svg width="50" height="60" viewBox="0 0 50 60"><rect x="14" y="6" width="30" height="48" rx="3" fill="none" stroke="#fff" stroke-width="2.4"/><rect x="4" y="10" width="10" height="40" rx="3" fill="none" stroke="#fff" stroke-width="2.4"/><rect x="19" y="11" width="20" height="9" fill="#fff"/><g fill="#fff"><rect x="19" y="25" width="5" height="4"/><rect x="27" y="25" width="5" height="4"/><rect x="35" y="25" width="5" height="4"/><rect x="19" y="33" width="5" height="4"/><rect x="27" y="33" width="5" height="4"/><rect x="35" y="33" width="5" height="4"/><rect x="19" y="41" width="5" height="4"/><rect x="27" y="41" width="5" height="4"/><rect x="35" y="41" width="5" height="4"/></g></svg></div>
  <h3>Phone Systems</h3>
  <p>Sales – As an Veltra and Orvane partner we can consult with you to ensure you maximise...</p>
  <div class="btn">Read more</div>
</div>

<h2 class="abs block-title heading" style="left:80px;top:1642px">Latest <span>News</span></h2>
<article class="news-item" style="top:1700px">
  <div class="thumb"><div role="img" aria-label="Colleagues working together at a desk"></div></div>
  <h4>Lorem Ipsum is simply dumm</h4>
  <p>Lorem Ipsum is simply dummy text of the printing and typesetting industry. Lorem Ipsum has been the</p>
  <a>Learn more</a>
</article>
<article class="news-item" style="top:1825px">
  <div class="thumb"><div role="img" aria-label="Colleagues working together at a desk"></div></div>
  <h4>Lorem Ipsum is simply dumm</h4>
  <p>Lorem Ipsum is simply dummy text of the printing and typesetting industry. Lorem Ipsum has been the</p>
  <a>Learn more</a>
</article>

<h2 class="abs block-title heading" style="left:624px;top:1642px">Get a Free <span>Quote</span></h2>
<div class="field" style="left:624px;top:1698px;width:245px;height:41px">Name</div>
<div class="field" style="left:878px;top:1698px;width:245px;height:41px">E-Mail</div>
<div class="field" style="left:624px;top:1746px;width:245px;height:41px">Phone</div>
<div class="field" style="left:878px;top:1746px;width:245px;height:41px">Subject</div>
<div class="field" style="left:624px;top:1792px;width:499px;height:73px">Message</div>
<div class="btn" style="left:624px;top:1876px;width:124px;height:51px;font-size:19px">Submit</div>

<section class="abs testimonial">
  <div class="quote-mark" style="left:158px;top:62px">&ldquo;</div>
  <div class="avatar" role="img" aria-label="Portrait photo of the client"></div>
  <p class="quote-text">"Lorem Ipsum is simply dummy text of the printing and typesetting industry. Lorem Ipsum has been the industry's standard dummy text ever since the 1500s, when an unknown printer took a galley of type and scrambled it to make a type specimen book."</p>
  <div class="quote-name">Mara Jennings, <small>CEO - Company Name</small></div>
  <div class="quote-mark" style="left:682px;top:160px">&rdquo;</div>
</section>

<footer>
  <div class="abs foot-title" style="left:80px;top:2239px">Quick Links <i></i></div>
  <ul class="abs quick-links">
    <li class="active">Home</li><li>About</li><li>Services</li><li>News</li><li style="border:0">Contact</li>
  </ul>
  <div class="abs foot-title" style="left:344px;top:2239px">Contact Info <i></i></div>
  <div class="contact-row" style="top:2281px">
    <svg width="24" height="20" viewBox="0 0 24 20"><path d="M2 4l6-2 8 3 6-2v13l-6 2-8-3-6 2z M8 2v13 M16 5v13" fill="none" stroke="#0a5796" stroke-width="1.5"/></svg>
    <span>Ground Floor 14, Marlow St,<br>East Kendra,<br>KO 4120</span>
  </div>
  <div class="contact-row" style="top:2362px">
    <svg width="24" height="22" viewBox="0 0 24 24"><path d="M6.6 10.8a15.1 15.1 0 0 0 6.6 6.6l2.2-2.2c.3-.3.7-.4 1-.2 1.1.4 2.3.6 3.6.6.6 0 1 .4 1 1V20c0 .6-.4 1-1 1A17 17 0 0 1 3 4c0-.6.4-1 1-1h3.5c.6 0 1 .4 1 1 0 1.3.2 2.5.6 3.6.1.3 0 .7-.2 1z" fill="none" stroke="#0a5796" stroke-width="1.6"/></svg>
    <span>555 0142 770</span>
  </div>
  <div class="contact-row" style="top:2403px">
    <svg width="24" height="20" viewBox="0 0 24 20"><rect x="2" y="3" width="20" height="14" rx="1" fill="none" stroke="#0a5796" stroke-width="1.6"/><path d="M2 4l10 8 10-8" fill="none" stroke="#0a5796" stroke-width="1.6"/></svg>
    <span>info@harborlinkko.com</span>
  </div>
  <div class="abs map" role="img" aria-label="Street map showing the office location"></div>
  <div class="abs foot-brand">Harbor Link</div>
  <div class="abs social" aria-label="Social links"><span></span><span></span><span></span></div>
  <div class="abs copyright">&copy; <span>Harbor Link</span> - 2016. All Rights Reserved.</div>
</footer>

</body>
</html>
```